Business card design

Hi,
I need to have a business card design based on the current logo.
If competitive I not put it out to everyone.

It can be single of double sided

Target Market(s)

Food businesses

Industry/Entity Type

Food Manufacturing

Contact Information for Business Card

Details will on card will be as follows Name = Marcus Pell Email = Marcus@BrimKitchens.com.au Phone = 0418562307 Address = 57 Tallowmere Road , Fortitude Valley QLD 4006 Australia

Font styles to use
Other font styles liked:
• based on two fonts - Adelle & Museo

Requirements
Must have
• Based on the on switch concept

```html
<!DOCTYPE html>
<html lang="en">
<head>
<meta charset="utf-8">
<title>BrimKitchens Business Card</title>
<link rel="stylesheet" href="https://fonts.googleapis.com/css2?family=Zilla+Slab:wght@400;600;700&display=swap">
<style>
  :root {
    --bg: #ececea;
    --paper: #ffffff;
    --brand-red: #ea2548;
    --brand-red-light: #f1667e;
    --cocoa: #3b2628;
    --cocoa-light: #5a4446;
    --ink: #3b2628;
    --white: #ffffff;
  }
  * { box-sizing: border-box; margin: 0; padding: 0; }
  html, body {
    width: 1200px; height: 1200px; overflow: hidden;
    background: var(--bg);
    font-family: "Zilla Slab", Georgia, serif;
  }
  .sheet { position: relative; width: 1200px; height: 1200px; }
  .card {
    position: absolute; left: 180px; width: 840px; height: 480px;
    background: var(--paper); overflow: hidden;
    box-shadow: 0 14px 34px rgba(0,0,0,0.16);
  }
  .card--front { top: 80px; }
  .card--back { top: 640px; }

  .brand {
    position: absolute; display: flex; align-items: center; gap: 18px;
    color: var(--ink); font-weight: 700; letter-spacing: 1px;
  }
  .brand__dot { border-radius: 50%; background: var(--brand-red); flex: none; }
  .brand__name { line-height: 1; }

  /* Front */
  .card--front .brand { left: 0; right: 0; top: 120px; justify-content: center; }
  .card--front .brand__dot { width: 60px; height: 60px; }
  .card--front .brand__name { font-size: 78px; }
  .front-band {
    position: absolute; left: 0; right: 0; bottom: 0; height: 170px;
    background: linear-gradient(90deg, var(--brand-red-light), var(--brand-red) 45%);
  }
  .tagline--band {
    position: absolute; right: 70px; bottom: 40px;
    color: var(--white); font-size: 36px; font-weight: 700; white-space: nowrap;
  }

  /* Back */
  .card--back .brand { left: 150px; top: 56px; }
  .card--back .brand__dot { width: 46px; height: 46px; }
  .card--back .brand__name { font-size: 64px; }
  .tagline--small {
    position: absolute; right: 212px; top: 130px;
    font-size: 19px; font-weight: 600; color: var(--ink); white-space: nowrap;
  }
  .back-panel {
    position: absolute; left: 0; right: 0; bottom: 0; height: 290px;
    background: linear-gradient(90deg, var(--cocoa-light), var(--cocoa) 35%);
    color: var(--white);
  }
  .person { position: absolute; left: 60px; top: 50px; }
  .person__name {
    font-size: 40px; font-weight: 700; padding-bottom: 12px;
    border-bottom: 3px solid var(--brand-red); display: inline-block; padding-right: 40px;
  }
  .contact-list { list-style: none; margin-top: 22px; }
  .contact-list li {
    display: flex; align-items: center; gap: 14px;
    font-size: 25px; margin-bottom: 14px; white-space: nowrap;
  }
  .icon { width: 22px; height: 22px; flex: none; fill: var(--brand-red); }
  .address {
    position: absolute; left: 530px; top: 60px;
    display: flex; gap: 12px; font-size: 24px; line-height: 1.5; white-space: nowrap;
  }
  .address .icon { margin-top: 6px; }
</style>
</head>
<body>
<main class="sheet">
  <section class="card card--front" aria-label="Business card front">
    <div class="brand">
      <span class="brand__dot"></span>
      <span class="brand__name">BrimKitchens</span>
    </div>
    <div class="front-band">
      <p class="tagline tagline--band">Fresh Kitchen Meals On Call</p>
    </div>
  </section>

  <section class="card card--back" aria-label="Business card back">
    <div class="brand">
      <span class="brand__dot"></span>
      <span class="brand__name">BrimKitchens</span>
    </div>
    <p class="tagline tagline--small">Fresh Kitchen Meals On Call</p>
    <div class="back-panel">
      <div class="person">
        <h1 class="person__name">Marcus Pell</h1>
        <ul class="contact-list">
          <li>
            <svg class="icon" viewBox="0 0 24 24" aria-hidden="true"><path d="M2 9l10-6 10 6v12H2z M4 10l8 5 8-5"/></svg>
            Marcus@BrimKitchens.com.au
          </li>
          <li>
            <svg class="icon" viewBox="0 0 24 24" aria-hidden="true"><path d="M6.6 10.8a15 15 0 006.6 6.6l2.2-2.2a1 1 0 011-.25 11.4 11.4 0 003.6.57 1 1 0 011 1V20a1 1 0 01-1 1A17 17 0 013 4a1 1 0 011-1h3.5a1 1 0 011 1 11.4 11.4 0 00.57 3.6 1 1 0 01-.25 1z"/></svg>
            0418562307
          </li>
        </ul>
      </div>
      <div class="address">
        <svg class="icon" viewBox="0 0 24 24" aria-hidden="true"><path d="M12 2a7 7 0 00-7 7c0 5.2 7 13 7 13s7-7.8 7-13a7 7 0 00-7-7zm0 9.5A2.5 2.5 0 1112 6.5a2.5 2.5 0 010 5z"/></svg>
        <p>57 Tallowmere Road ,<br>Marrowind Heights<br>QLD 4193 Australia</p>
      </div>
    </div>
  </section>
</main>
</body>
</html>
```